vorp business card design

vorp is an incubator within TRW Mediaworks focused on unlocking the potential in underserved niche micro-verticals on the web. our mission is to rapidly develop and foster emerging micro-verticals bc they are ripe for growth - building interesting and trusted content experiences with unqiue, useful and cutting-edge delivery methods.please do all copy (except for TRW Mediaworks, which must look as typed here and in logo) in all lowercase. Also please use spaces between phone # extensions not dashes or periods. I have attached all variations of the logo.
Industry/Entity Type
Business
Contact Information for Business Card
dale fenwright, ceo www.vorp.example 218 9th avenue 3rd floor oakland ca 94610 415 602 0002m 510 985 7966d dale.fenwright@vorp.example
Look and feel

```html
<!DOCTYPE html>
<html lang="en">
<head>
<meta charset="utf-8">
<title>vorp business card</title>
<link rel="stylesheet" href="https://fonts.googleapis.com/css2?family=Open+Sans:wght@400;700&display=swap">
<style>
  :root {
    --page: #e9e9e7;
    --card: #ffffff;
    --ink: #1f1f1f;
    --teal: #0f6d70;
    --shadow: rgba(0, 0, 0, 0.14);
  }
  * { box-sizing: border-box; margin: 0; padding: 0; }
  html, body {
    width: 1054px;
    height: 1200px;
    overflow: hidden;
    background: var(--page);
    font-family: "Open Sans", sans-serif;
    color: var(--ink);
  }
  .sheet {
    position: relative;
    width: 1054px;
    height: 1200px;
    display: flex;
    justify-content: center;
    align-items: center;
    gap: 44px;
  }
  .card {
    position: relative;
    width: 460px;
    height: 805px;
    background: var(--card);
    box-shadow: 0 6px 22px var(--shadow);
    overflow: hidden;
  }

  /* front */
  .brand {
    position: absolute;
    left: 62px;
    top: 250px;
  }
  .brand-row {
    display: flex;
    align-items: flex-start;
    gap: 8px;
  }
  .brand-name {
    font-size: 104px;
    font-weight: 700;
    line-height: 0.9;
    letter-spacing: -2px;
    color: var(--ink);
  }
  .brand-dot {
    width: 22px;
    height: 22px;
    border-radius: 50%;
    background: var(--teal);
    margin-top: 6px;
  }
  .brand-tagline {
    margin-top: 10px;
    font-size: 15px;
    letter-spacing: 0.3px;
    color: var(--ink);
  }
  .divider {
    position: absolute;
    left: 176px;
    top: 470px;
    width: 246px;
    height: 2px;
    background: var(--teal);
  }
  .person {
    position: absolute;
    left: 176px;
    top: 428px;
    line-height: 1.1;
  }
  .person-name { font-size: 25px; }
  .person-title { font-size: 19px; }
  .contact {
    position: absolute;
    left: 176px;
    top: 500px;
    font-size: 21px;
    line-height: 1.3;
  }
  .address {
    position: absolute;
    left: 176px;
    top: 650px;
    font-size: 21px;
    line-height: 1.3;
  }

  /* back */
  .back-mark {
    position: absolute;
    right: -60px;
    top: 330px;
    width: 220px;
    height: 220px;
    border-radius: 50%;
    background: var(--teal);
  }
</style>
</head>
<body>
  <main class="sheet">
    <section class="card card-front" aria-label="card front">
      <div class="brand">
        <div class="brand-row">
          <span class="brand-name">vorp</span>
          <span class="brand-dot"></span>
        </div>
        <p class="brand-tagline">a TRW Mediaworks incubator</p>
      </div>
      <div class="person">
        <p class="person-name">dale fenwright</p>
      </div>
      <div class="divider"></div>
      <div class="contact">
        <p class="person-title">ceo</p>
        <p>415 738 1194 m</p>
        <p>510 247 3318 d</p>
        <p>dale@vorp.example</p>
        <p>www.vorp.example</p>
      </div>
      <div class="address">
        <p>218 9th avenue 3rd floor</p>
        <p>oakland ca 94610</p>
      </div>
    </section>

    <section class="card card-back" aria-label="card back">
      <div class="back-mark"></div>
    </section>
  </main>
</body>
</html>
```